Welding Fabrication and Inspection Business Card Design

Welding Fabrication and Inspection Services,

Business

Industrial Machinery ServicesMohammed Rahim30 Ballarat Street, Mount Gravatt East.4122.QLD

```html
<!DOCTYPE html>
<html lang="en">
<head>
<meta charset="utf-8">
<title>Tarnwell Forge Services – Business Card</title>
<link rel="stylesheet" href="https://fonts.googleapis.com/css2?family=Roboto:wght@400;500;700&display=swap">
<style>
  :root {
    --page-bg: #e9e7e3;
    --card-white: #ffffff;
    --card-grey: #d9d9d9;
    --ink: #1b1b1b;
    --ink-soft: #3a3a3a;
    --muted: #8a8a8a;
    --dark-1: #0c0c0c;
    --dark-2: #2a2a2a;
    --gloss: #5a5a5a;
    --brand-light: #e6e6e6;
  }
  * { box-sizing: border-box; margin: 0; padding: 0; }
  html, body { width: 1200px; height: 950px; overflow: hidden; }
  body {
    background: var(--page-bg);
    font-family: "Roboto", Arial, sans-serif;
    display: flex;
    flex-direction: column;
    align-items: center;
    justify-content: center;
    gap: 30px;
  }
  .card {
    position: relative;
    width: 760px;
    height: 434px;
    overflow: hidden;
    box-shadow: 0 6px 18px rgba(0,0,0,0.18);
  }

  /* Back side */
  .card-back {
    background:
      linear-gradient(90deg, transparent 68%, rgba(255,255,255,0.05) 74%, var(--gloss) 78%, rgba(255,255,255,0.08) 82%, transparent 90%),
      linear-gradient(160deg, var(--dark-2) 0%, var(--dark-1) 60%, #1d1d1d 100%);
  }
  .back-brand {
    position: absolute;
    left: 0; right: 0;
    top: 180px;
    text-align: center;
    color: var(--brand-light);
    font-weight: 700;
    font-size: 34px;
    letter-spacing: 0.5px;
  }
  .back-web {
    position: absolute;
    left: 0; right: 0;
    top: 246px;
    display: flex;
    justify-content: center;
    align-items: center;
    gap: 14px;
    color: #bdbdbd;
    font-size: 17px;
  }
  .back-web .rule { width: 60px; height: 1px; background: #9a9a9a; }

  /* Front side */
  .card-front {
    background: linear-gradient(160deg, var(--card-white) 0%, var(--card-white) 45%, var(--card-grey) 100%);
    color: var(--ink);
  }
  .brand-block {
    position: absolute;
    top: 0;
    left: 470px;
    width: 205px;
    height: 92px;
    background: linear-gradient(180deg, #3a3a3a 0%, #1a1a1a 100%);
  }
  .brand-name {
    position: absolute;
    top: 112px;
    left: 420px;
    width: 310px;
    text-align: center;
    font-weight: 700;
    font-size: 21px;
    color: var(--ink);
  }
  .holder {
    position: absolute;
    left: 44px;
    top: 118px;
  }
  .holder-name { font-size: 30px; font-weight: 500; color: var(--ink); }
  .holder-role { font-size: 17px; color: var(--muted); margin-top: 4px; }
  .contacts {
    position: absolute;
    left: 44px;
    top: 210px;
    list-style: none;
    font-size: 18px;
    color: var(--ink-soft);
  }
  .contacts li { display: flex; align-items: center; gap: 10px; margin-bottom: 6px; }
  .contacts svg { width: 16px; height: 16px; fill: var(--ink); flex: none; }
  .address {
    position: absolute;
    right: 44px;
    bottom: 44px;
    text-align: right;
    font-size: 19px;
    line-height: 1.35;
    color: var(--ink-soft);
  }
</style>
</head>
<body>

  <section class="card card-back" aria-label="Card back">
    <div class="back-brand">Tarnwell Forge Services</div>
    <div class="back-web"><span>www.TarnwellForgeServices.com</span><span class="rule"></span></div>
  </section>

  <section class="card card-front" aria-label="Card front">
    <div class="brand-block"></div>
    <div class="brand-name">Tarnwell Forge Services</div>

    <div class="holder">
      <div class="holder-name">Khalid Nasser</div>
      <div class="holder-role">President</div>
    </div>

    <ul class="contacts">
      <li>
        <svg viewBox="0 0 16 16" aria-hidden="true"><path d="M3 2h3l1.2 3-1.8 1.2a8 8 0 0 0 4.4 4.4L11 8.8l3 1.2v3a1 1 0 0 1-1 1A12 12 0 0 1 2 3a1 1 0 0 1 1-1z"/></svg>
        555 014 2287
      </li>
      <li>
        <svg viewBox="0 0 16 16" aria-hidden="true"><path d="M1 3h14v10H1z M2 4.2v.3l6 4 6-4v-.3z" fill-rule="evenodd"/></svg>
        khalid@tarnwellforge.com
      </li>
      <li>
        <svg viewBox="0 0 16 16" aria-hidden="true"><circle cx="8" cy="8" r="7"/><path d="M4 6h8M4 10h8M8 1v14" stroke="#fff" stroke-width="1" fill="none"/></svg>
        www.tarnwellforge.com
      </li>
    </ul>

    <address class="address" style="font-style:normal">
      17 Corrowen Street<br>
      Ridgemont East. 4170.QLD
    </address>
  </section>

</body>
</html>
```